Brisden + Mallow Chocolate Cafe - Takeaway Packaging

Packaging Design required for premium chocolate cafe brand

1. 8 oz & 12 oz takeaway cups - ideally logo in gold foil - innovative luxury / premium look - designed to fit the same lid on both cup size.
2. Paper bag range for chocolate products - two sizes (180mm(w) x 90mm(d) x280mm(h)) & (360mm (w) x 120mm (d) x 310mm (h)).
3. Paper napkins - 15cm square cocktail napkin
4. Branded Greaseproof paper wrap for sandwiches
5. Branded Greaseproof Baking Paper for muffins
6. Branded Takeaway Cake boxes
7. Branded Greaseproof paper loose chocolate bags - two sizes (100mm (w) x 30mm (d) x 195mm (h) and (100mm (w) x 30mm (d) x 100mm (h))

See detailed brand guidelines and logo samples attached.
Happy for alternative Colour scheme proposals - other than colours set out in brand guidelines.

Detailed B+M Takeaway Cup brief & Paperbag Briefs attached.

Target Market(s)

Premium Retail / Cafe

Industry/Entity Type

Chocolate Retail / Cafe

Font styles to use
Other font styles liked:
• Raleway Light, LATO Clean & Trajan Pro Bold

Requirements
Must have
• Scandi, Modern, Premium, Luxury feel & design
Nice to have
• Logo in Gold foil

```html
<!DOCTYPE html>
<html lang="en">
<head>
<meta charset="utf-8">
<title>Brisden + Mallow Chocolate Cafe – Greaseproof Wrap Pattern</title>
<link href="https://fonts.googleapis.com/css2?family=Raleway:wght@300&display=swap" rel="stylesheet">
<style>
  :root {
    --olive-deep: #55603a;
    --olive-mid: #66714a;
    --paper-tone: #8f9874;
    --ink-white: #ffffff;
    --tile: 101px;
  }
  html, body {
    margin: 0;
    padding: 0;
    width: 1200px;
    height: 673px;
    overflow: hidden;
    background: var(--olive-deep);
  }
  .wrap-sheet {
    position: relative;
    width: 1200px;
    height: 673px;
    overflow: hidden;
    font-family: "Raleway", sans-serif;
    font-weight: 300;
    color: var(--ink-white);
  }
  .backdrop {
    position: absolute;
    inset: 0;
    background:
      radial-gradient(ellipse 420px 300px at 560px 330px, var(--paper-tone) 0%, rgba(143,152,116,0.55) 55%, rgba(143,152,116,0) 100%),
      linear-gradient(135deg, var(--olive-mid) 0%, var(--olive-deep) 100%);
  }
  .monogram-tile {
    position: absolute;
    width: var(--tile);
    height: var(--tile);
    box-sizing: border-box;
    border: 1.5px solid var(--ink-white);
    display: flex;
    align-items: center;
    justify-content: center;
    font-size: 22px;
  }
  .brand-name {
    position: absolute;
    left: 330px;
    top: 270px;
    width: 272px;
    margin: 0;
    text-align: center;
    font-size: 16px;
    line-height: 1.35;
  }
  .custom-text {
    position: absolute;
    left: 798px;
    top: 383px;
    margin: 0;
    font-size: 15px;
  }
</style>
</head>
<body>
<main class="wrap-sheet">
  <div class="backdrop" role="img" aria-label="Photo of overlapping greaseproof paper sheets on an olive green surface"></div>

  <!-- row 1 -->
  <div class="monogram-tile" style="left:81px;top:86px">B+M</div>
  <div class="monogram-tile" style="left:216px;top:86px">B+M</div>
  <div class="monogram-tile" style="left:350px;top:86px">B+M</div>
  <div class="monogram-tile" style="left:482px;top:86px">B+M</div>
  <div class="monogram-tile" style="left:616px;top:86px">B+M</div>
  <div class="monogram-tile" style="left:747px;top:86px">B+M</div>
  <div class="monogram-tile" style="left:881px;top:86px">B+M</div>
  <div class="monogram-tile" style="left:1012px;top:86px">B+M</div>

  <!-- row 2 -->
  <div class="monogram-tile" style="left:81px;top:214px">B+M</div>
  <div class="monogram-tile" style="left:216px;top:214px">B+M</div>
  <p class="brand-name">Brisden + Mallow Chocolate Cafe</p>
  <div class="monogram-tile" style="left:616px;top:214px">B+M</div>
  <div class="monogram-tile" style="left:747px;top:214px">B+M</div>
  <div class="monogram-tile" style="left:881px;top:214px">B+M</div>
  <div class="monogram-tile" style="left:1012px;top:214px">B+M</div>

  <!-- row 3 -->
  <div class="monogram-tile" style="left:81px;top:342px">B+M</div>
  <div class="monogram-tile" style="left:216px;top:342px">B+M</div>
  <div class="monogram-tile" style="left:350px;top:342px">B+M</div>
  <div class="monogram-tile" style="left:482px;top:342px">B+M</div>
  <div class="monogram-tile" style="left:616px;top:342px">B+M</div>
  <p class="custom-text">Add custom text</p>
  <div class="monogram-tile" style="left:1012px;top:342px">B+M</div>

  <!-- row 4 -->
  <div class="monogram-tile" style="left:81px;top:474px">B+M</div>
  <div class="monogram-tile" style="left:216px;top:474px">B+M</div>
  <div class="monogram-tile" style="left:350px;top:474px">B+M</div>
  <div class="monogram-tile" style="left:482px;top:474px">B+M</div>
  <div class="monogram-tile" style="left:616px;top:474px">B+M</div>
  <div class="monogram-tile" style="left:747px;top:474px">B+M</div>
  <div class="monogram-tile" style="left:881px;top:474px">B+M</div>
  <div class="monogram-tile" style="left:1012px;top:474px">B+M</div>
</main>
</body>
</html>
```